Business Card Design

We need a new buisness card designed for a new company in Darwin
We dig trenchs and lay pipes for the communication industry,Electrical industry, Teleco industry,
We also do some concrete works as well,
And small excavation work
Industry/Entity Type
Communication
Contact Information for Business Card
Tolvani Contracting PTY LTD
Pit and Pipe installations
Trenching,Excavations, Concreting ,
civil works, unistrut soloutions ,over thirty years experiance
WE DIG DEEP SO YOU DON'T HAVE TO
Contact Glen 0451936024 ps
(would like name to stand out somehow in another text or graphic sort of a way am also looking for some sort of slogan) will most likely be a red card with black writing

```html
<!DOCTYPE html>
<html lang="en">
<head>
<meta charset="utf-8">
<title>Tolvani Contracting – Business Card</title>
<link rel="stylesheet" href="https://fonts.googleapis.com/css2?family=Tinos:wght@400;700&family=Crimson+Text&family=Open+Sans&display=swap">
<style>
  :root {
    --card-red: #fe0000;
    --ink-black: #0a0a0a;
  }
  html, body {
    margin: 0;
    padding: 0;
    width: 1200px;
    height: 741px;
    overflow: hidden;
    background: var(--card-red);
  }
  .card {
    position: relative;
    width: 1200px;
    height: 741px;
    background: var(--card-red);
    overflow: hidden;
  }
  .company-name {
    position: absolute;
    left: 38px;
    top: 4px;
    margin: 0;
    font-family: "Tinos", serif;
    font-weight: 700;
    font-size: 120px;
    line-height: 1;
    color: var(--ink-black);
    white-space: nowrap;
    transform: scaleX(0.755);
    transform-origin: left top;
    letter-spacing: -1px;
  }
  .company-suffix {
    position: absolute;
    left: 580px;
    top: 129px;
    font-family: "Tinos", serif;
    font-weight: 700;
    font-size: 44px;
    line-height: 1;
    color: var(--ink-black);
    letter-spacing: 4px;
  }
  .contact-block {
    position: absolute;
    left: 862px;
    top: 0;
    width: 338px;
    height: 191px;
    background: var(--ink-black);
    text-align: center;
  }
  .contact-name {
    margin: 18px 0 0;
    font-family: "Tinos", serif;
    font-weight: 700;
    font-size: 92px;
    line-height: 1;
    color: var(--card-red);
  }
  .contact-phone {
    margin: 16px 0 0;
    font-family: "Open Sans", sans-serif;
    font-size: 36px;
    line-height: 1;
    color: var(--card-red);
  }
  .services {
    position: absolute;
    left: 97px;
    top: 252px;
    margin: 0;
    padding: 0;
    list-style: none;
  }
  .service-item {
    display: flex;
    align-items: center;
    height: 71.5px;
    font-family: "Crimson Text", serif;
    font-size: 67px;
    line-height: 1;
    color: var(--ink-black);
    white-space: nowrap;
  }
  .tick-icon {
    width: 42px;
    height: 34px;
    margin-right: 28px;
    flex: none;
  }
  .slogan-band {
    position: absolute;
    left: 0;
    top: 630px;
    width: 1200px;
    height: 111px;
    background: var(--ink-black);
  }
  .slogan {
    position: absolute;
    left: 62px;
    top: 33px;
    margin: 0;
    font-family: "Tinos", serif;
    font-weight: 700;
    font-size: 46px;
    line-height: 1;
    color: var(--card-red);
    white-space: nowrap;
    letter-spacing: 2.5px;
  }
</style>
</head>
<body>
  <div class="card">
    <h1 class="company-name">Tolvani Contracting</h1>
    <div class="company-suffix">PTY LTD</div>

    <div class="contact-block">
      <p class="contact-name">Glen</p>
      <p class="contact-phone">0451936024</p>
    </div>

    <ul class="services">
      <li class="service-item"><svg class="tick-icon" viewBox="0 0 42 34" aria-hidden="true"><path d="M2 18 L9 11 L16 18 L33 1 L40 8 L16 32 Z" fill="#0a0a0a"/></svg>Pit and Pipe installations,</li>
      <li class="service-item"><svg class="tick-icon" viewBox="0 0 42 34" aria-hidden="true"><path d="M2 18 L9 11 L16 18 L33 1 L40 8 L16 32 Z" fill="#0a0a0a"/></svg>Trenching,</li>
      <li class="service-item"><svg class="tick-icon" viewBox="0 0 42 34" aria-hidden="true"><path d="M2 18 L9 11 L16 18 L33 1 L40 8 L16 32 Z" fill="#0a0a0a"/></svg>Excavations,</li>
      <li class="service-item"><svg class="tick-icon" viewBox="0 0 42 34" aria-hidden="true"><path d="M2 18 L9 11 L16 18 L33 1 L40 8 L16 32 Z" fill="#0a0a0a"/></svg>Concreting civil works,</li>
      <li class="service-item"><svg class="tick-icon" viewBox="0 0 42 34" aria-hidden="true"><path d="M2 18 L9 11 L16 18 L33 1 L40 8 L16 32 Z" fill="#0a0a0a"/></svg>Over thirty years experiance</li>
    </ul>

    <div class="slogan-band">
      <p class="slogan">WE DIG DEEP SO YOU DON'T HAVE TO</p>
    </div>
  </div>
</body>
</html>
```